Kelvaro.lu - Héritage en confiance

As a rule, most people plan everything meticulously down to the smallest detail, at least when it comes to aspects such as building a house, buying a car, or making major purchases. However, very few think about what is usually the single biggest “transaction” of their entire lives and make provisions for it. We are talking about inheritance – or, from the other perspective, inheriting. In any case, it is about estate planning.

Target Market(s)

Inheritance of a property - People that inheritated a property

Industry/Entity Type

Inheritance of a property - Real Estate

Coding

Coded - Design and coding required

Number of Pages Required

4 page

Font styles to use
Decorative

Colors
0054AA
0677BA
7BADD7
CADEEF
E8F1F8

Requirements
Must have
• Four different Navigation buttons: 1. Immobilier (if somebody inherated a house or flat) 2. Services (if people do not kow what to do) 3. Calculatrice (if people want to get an idea of the value of the house or flat) 4. Contact (to get in touch with us through a text form).
Nice to have
• Since visitors to this site may be in mourning, the website should be very user-friendly and welcoming.
Should not have
• Too bright, too many colors...

```html
<!DOCTYPE html>
<html lang="fr">
<head>
<meta charset="utf-8">
<title>Kelvaro.lu – Héritage en confiance</title>
<link href="https://fonts.googleapis.com/css2?family=Playfair+Display:ital,wght@0,400;0,700;1,400;1,700&family=Open+Sans:wght@400;600;700&display=swap" rel="stylesheet">
<style>
:root{
  --navy:#0054AA;
  --blue:#0677BA;
  --sky:#7BADD7;
  --pale:#CADEEF;
  --mist:#E8F1F8;
  --ink:#3c4650;
  --muted:#7a8590;
  --footer:#2f3338;
  --white:#ffffff;
}
*{margin:0;padding:0;box-sizing:border-box}
html,body{width:796px;height:1200px;overflow:hidden;background:var(--white)}
body{font-family:"Open Sans",Arial,sans-serif;color:var(--ink);font-size:9px;line-height:1.5}
.page{width:796px;height:1200px;display:flex;flex-direction:column}
.script{font-family:"Playfair Display",Georgia,serif;font-style:italic;font-weight:700;color:var(--blue)}

/* header */
.site-header{height:56px;flex:none;display:flex;align-items:center;justify-content:space-between;padding:0 60px;border-bottom:1px solid var(--mist)}
.brand{display:flex;align-items:center;gap:8px}
.brand-mark{width:14px;height:14px;background:var(--navy)}
.brand-name{font-family:"Open Sans",Arial,sans-serif;font-weight:700;font-size:20px;color:var(--navy);line-height:1}
.main-nav{display:flex;gap:22px;align-items:center}
.main-nav a{font-size:8.5px;font-weight:600;color:var(--ink);text-decoration:none;letter-spacing:.5px}
.main-nav a.active{color:var(--blue)}
.main-nav a.nav-cta{background:var(--blue);color:var(--white);padding:6px 14px;border-radius:14px}

/* hero */
.hero{height:250px;flex:none;position:relative;background:linear-gradient(100deg,#5e8a3a 0%,#a7b95a 35%,#d9d7a6 60%,#8aa867 100%)}
.hero-text{position:absolute;left:120px;top:42px;width:300px;color:var(--white)}
.hero-kicker{font-family:"Playfair Display",Georgia,serif;font-weight:700;font-size:17px}
.hero-title{font-family:"Playfair Display",Georgia,serif;font-style:italic;font-weight:700;font-size:27px;line-height:1.15;margin-top:2px}
.hero-lead{font-size:8.5px;margin-top:8px;width:270px;opacity:.95}

/* welcome */
.welcome{height:130px;flex:none;background:var(--mist);padding:16px 120px 0}
.welcome h2{font-size:26px;text-align:center;margin-bottom:10px}
.welcome-cols{display:flex;gap:40px}
.welcome-cols p{width:260px;font-size:8px;color:var(--muted)}
.guide h3{font-family:"Playfair Display",Georgia,serif;font-style:italic;font-size:11px;color:var(--ink);margin-bottom:3px}
.guide ul{list-style:none;font-size:8px;color:var(--muted);columns:2;column-gap:20px;width:300px}
.guide li::before{content:"• ";color:var(--blue)}

/* values */
.values{height:250px;flex:none;padding-top:20px;text-align:center}
.values h2{font-size:30px;margin-bottom:16px}
.value-cards{display:flex;justify-content:center;gap:12px}
.value-card{width:180px}
.value-photo{height:88px}
.value-photo.house{background:linear-gradient(135deg,#e7e2dc,#c44a3c 55%,#d9d2cb)}
.value-photo.seal{background:linear-gradient(135deg,#e9e3d6,#9c2d28 50%,#d8cbb4)}
.value-photo.calc{background:linear-gradient(135deg,#eef0f2,#b9c2ca 55%,#e5e7ea)}
.value-body{background:var(--blue);color:var(--white);padding:10px 10px 12px}
.value-body h3{font-family:"Playfair Display",Georgia,serif;font-style:italic;font-weight:700;font-size:16px}
.value-body p{font-size:7.5px;opacity:.9}
.value-btn{display:inline-block;margin-top:6px;background:var(--navy);font-size:7px;padding:3px 12px;border-radius:8px;color:var(--white)}

/* quote */
.quote{height:90px;flex:none;display:flex;align-items:center;justify-content:center;text-align:center;border-top:1px solid var(--mist);border-bottom:1px solid var(--mist)}
.quote p{font-size:20px;line-height:1.25;font-weight:400}

/* team */
.team{height:230px;flex:none;padding-top:14px;text-align:center;position:relative}
.team h2{font-size:27px}
.team-intro{width:560px;margin:4px auto 10px;font-size:7.5px;color:var(--muted)}
.team-row{display:flex;justify-content:center;height:140px;position:relative}
.team-row::after{content:"";position:absolute;left:0;right:0;bottom:0;height:10px;background:var(--blue)}
.member{width:96px;height:130px;background:linear-gradient(180deg,#e4e7ea,#b6bec6)}
.member:nth-child(even){background:linear-gradient(180deg,#dfe3e6,#8f9aa5)}
.member-tag{position:absolute;left:112px;top:56px;background:var(--navy);color:var(--white);font-size:7px;padding:3px 8px;text-align:left}

/* footer */
.site-footer{flex:1;background:var(--footer);color:#c4c9ce;display:flex;align-items:flex-start;gap:30px;padding:18px 60px 0;font-size:7.5px}
.site-footer h4{color:var(--sky);font-size:9px;margin-bottom:6px;font-weight:600}
.footer-nav{width:90px}
.footer-nav ul{list-style:none}
.footer-contact{width:130px}
.contact-form{width:230px;display:grid;grid-template-columns:1fr 1fr;grid-auto-rows:15px;gap:5px;align-content:start}
.contact-form h4{grid-column:1/3;margin-bottom:0;line-height:15px}
.field{background:var(--white);color:var(--muted);padding:0 5px;line-height:15px;height:15px;font-size:7px}
.send{background:var(--blue);color:var(--white);font-size:7px;line-height:15px;text-align:center;height:15px}
.footer-legal{flex:1;text-align:right}
.socials{display:flex;gap:6px;justify-content:flex-end;margin-top:8px}
.socials span{width:16px;height:16px;border-radius:50%;background:var(--blue)}
.socials span:nth-child(2){background:var(--sky)}
</style>
</head>
<body>
<div class="page">

  <header class="site-header">
    <div class="brand">
      <span class="brand-mark"></span>
      <span class="brand-name">Kelvaro.lu</span>
    </div>
    <nav class="main-nav">
      <a class="active" href="#">HOME</a>
      <a href="#">IMMOBILIER</a>
      <a href="#">SERVICES</a>
      <a href="#">CALCULATRICE</a>
      <a class="nav-cta" href="#">CONTACT</a>
    </nav>
  </header>

  <section class="hero" role="img" aria-label="Photo : une main transmet une clé ancienne à une autre main sur fond de verdure">
    <div class="hero-text">
      <div class="hero-kicker">Héritage d'un bien immobilier:</div>
      <div class="hero-title">Qu'est-ce qui est vraiment important ?</div>
      <p class="hero-lead">Nous vous accompagnons avec calme et clarté dans chaque étape, de l'évaluation du bien jusqu'aux démarches de succession.</p>
    </div>
  </section>

  <section class="welcome">
    <h2 class="script">Bienvenue Sur Kelvaro.lu</h2>
    <div class="welcome-cols">
      <p>Nous comprenons que l'héritage d'un bien immobilier peut survenir à un moment difficile. Notre équipe vous écoute, vous conseille et vous aide à prendre des décisions sereines, pas à pas, avec respect.</p>
      <div class="guide">
        <h3>Nous vous guidons sur:</h3>
        <ul>
          <li>La gestion d'un bien hérité</li>
          <li>Les démarches fiscales</li>
          <li>L'estimation de la valeur</li>
          <li>La vente ou la location</li>
          <li>Le conseil juridique</li>
        </ul>
      </div>
    </div>
  </section>

  <section class="values">
    <h2 class="script">Nous préservons les valeurs.</h2>
    <div class="value-cards">
      <article class="value-card">
        <div class="value-photo house" role="img" aria-label="Photo : petite maison rouge tenue entre deux mains"></div>
        <div class="value-body">
          <h3>Immobilier</h3>
          <p>Maison ou appartement hérité</p>
          <span class="value-btn">En savoir plus</span>
        </div>
      </article>
      <article class="value-card">
        <div class="value-photo seal" role="img" aria-label="Photo : document scellé à la cire rouge"></div>
        <div class="value-body">
          <h3>Services</h3>
          <p>Que faire maintenant ?</p>
          <span class="value-btn">En savoir plus</span>
        </div>
      </article>
      <article class="value-card">
        <div class="value-photo calc" role="img" aria-label="Photo : calculatrice et documents sur un bureau"></div>
        <div class="value-body">
          <h3>Calculatrice</h3>
          <p>Estimez la valeur du bien</p>
          <span class="value-btn">En savoir plus</span>
        </div>
      </article>
    </div>
  </section>

  <section class="quote">
    <p class="script">“Anticiper, c'est préserver. Avec Kelvaro.lu,<br>vous n'êtes pas seuls face à l'héritage.”</p>
  </section>

  <section class="team">
    <h2 class="script">Notre équipe</h2>
    <p class="team-intro">Des conseillers, juristes et experts immobiliers réunis pour vous accompagner avec bienveillance. Chacun apporte son savoir-faire afin que votre héritage reste une source de sérénité.</p>
    <div class="team-row">
      <div class="member" role="img" aria-label="Portrait d'un conseiller"></div>
      <div class="member" role="img" aria-label="Portrait d'une conseillère"></div>
      <div class="member" role="img" aria-label="Portrait d'un juriste"></div>
      <div class="member" role="img" aria-label="Portrait d'une experte immobilière"></div>
      <div class="member" role="img" aria-label="Portrait d'un notaire"></div>
      <div class="member" role="img" aria-label="Portrait d'un conseiller financier"></div>
      <div class="member" role="img" aria-label="Portrait d'une assistante"></div>
      <div class="member-tag">Marc Weber<br>Conseiller</div>
    </div>
  </section>

  <footer class="site-footer">
    <div class="footer-nav">
      <h4>Navigation</h4>
      <ul>
        <li>Home</li>
        <li>Immobilier</li>
        <li>Services</li>
        <li>Calculatrice</li>
        <li>Contact</li>
      </ul>
    </div>
    <div class="footer-contact">
      <h4>Contact</h4>
      <p>12 Rue des Tilleuls<br>L-1450 Luxembourg<br>Tél. +352 26 48 19 70<br>info@kelvaro.lu</p>
    </div>
    <form class="contact-form">
      <h4>Écrivez-nous</h4>
      <div class="field">Nom</div>
      <div class="field">Email</div>
      <div class="field">Téléphone</div>
      <div class="field">Sujet</div>
      <div class="field">Message</div>
      <div class="send">Envoyer</div>
    </form>
    <div class="footer-legal">
      <p>Copyright © 2024 Kelvaro.lu<br>All Rights Reserved</p>
      <div class="socials" aria-label="Réseaux sociaux"><span></span><span></span><span></span></div>
    </div>
  </footer>

</div>
</body>
</html>
```